Tallowmere Roofing Business Card

Need a business card with the logo that was designed here

Contact Information for Business Card

Name, Title, Phone, Email, Website, Company name

```html
<!DOCTYPE html>
<html lang="en">
<head>
<meta charset="utf-8">
<title>Tallowmere Roofing Business Card</title>
<link href="https://fonts.googleapis.com/css2?family=Montserrat:wght@500;600;700&display=swap" rel="stylesheet">
<style>
  :root {
    --brand-blue: #1170b5;
    --text-grey: #8a8c8e;
    --card-white: #ffffff;
    --backdrop: #2e2e2e;
  }
  * { margin: 0; padding: 0; box-sizing: border-box; }
  html, body {
    width: 1200px;
    height: 900px;
    overflow: hidden;
    background: var(--backdrop);
    font-family: "Montserrat", Arial, sans-serif;
  }
  .canvas {
    position: relative;
    width: 1200px;
    height: 900px;
  }
  .card {
    position: absolute;
    top: 302px;
    width: 513px;
    height: 295px;
    border-radius: 24px;
    overflow: hidden;
  }
  .card-front { left: 73px; background: var(--card-white); }
  .card-back { left: 616px; background: var(--brand-blue); }

  .wordmark {
    position: absolute;
    font-weight: 700;
    letter-spacing: 0.5px;
    line-height: 1.1;
    text-align: center;
  }
  .card-front .wordmark {
    right: 34px;
    top: 52px;
    width: 220px;
    font-size: 24px;
    color: var(--brand-blue);
  }
  .card-back .wordmark {
    left: 0;
    right: 0;
    top: 118px;
    font-size: 28px;
    color: var(--card-white);
  }
  .wordmark span { display: block; }

  .holder {
    position: absolute;
    left: 37px;
    top: 176px;
  }
  .holder-name {
    font-size: 13px;
    font-weight: 700;
    color: var(--brand-blue);
    letter-spacing: 0.3px;
  }
  .holder-title {
    margin-top: 3px;
    font-size: 13px;
    font-weight: 500;
    color: var(--text-grey);
    letter-spacing: 0.3px;
  }
  .contacts {
    position: absolute;
    left: 37px;
    top: 241px;
    list-style: none;
    font-size: 13px;
    font-weight: 500;
    color: var(--text-grey);
  }
  .contacts li {
    display: flex;
    align-items: center;
    gap: 5px;
    height: 18px;
  }
  .contacts svg { width: 11px; height: 11px; fill: var(--brand-blue); }
  .web-band {
    position: absolute;
    left: 268px;
    right: 0;
    top: 239px;
    height: 37px;
    background: var(--brand-blue);
    color: var(--card-white);
    font-size: 13px;
    font-weight: 500;
    display: flex;
    align-items: center;
    justify-content: center;
  }
</style>
</head>
<body>
<main class="canvas">
  <section class="card card-front" aria-label="Business card front">
    <div class="wordmark"><span>Tallowmere</span><span>Roofing</span></div>
    <div class="holder">
      <p class="holder-name">MARCUS HOLLANDER</p>
      <p class="holder-title">MANAGING DIRECTOR</p>
    </div>
    <ul class="contacts">
      <li>
        <svg viewBox="0 0 12 12" aria-hidden="true"><path d="M1 4c0-1.6 2.2-3 5-3s5 1.4 5 3l-2.3.6-.5-1.3H3.8l-.5 1.3zM2.5 6h7l.8 4.5H1.7z"/></svg>
        555 0142 7788
      </li>
      <li>
        <svg viewBox="0 0 12 12" aria-hidden="true"><path d="M1 3h10v.8L6 7 1 3.8zM1 5l5 3.2L11 5v4.5H1z"/></svg>
        info@tallowmereroofing.com
      </li>
    </ul>
    <div class="web-band">www.tallowmereroofing.com</div>
  </section>

  <section class="card card-back" aria-label="Business card back">
    <div class="wordmark"><span>Tallowmere</span><span>Roofing</span></div>
  </section>
</main>
</body>
</html>
```